Harwick Stone Meadows - Signature Golf Billboard

We need an Eye Catching Billboard for a local Golf Course. The board will be positioned in an area with a nearby competitor.

The Tag Line we would prefer to use is "Get Your Daily Dose of Iron." or just "Your Daily Dose of Iron"

The logo should be incorporated fairly large so passerby's easily can identify what course it is. (We have two logos, feel free to use whichever better suits the design needs.) We want to showcase the course in the image.

Billboard size is 8'Hx16'W

Target Market(s)

Males 24-60

Industry/Entity Type

Golf Course

Requirements
Must have
• Logo, Image(s) of the course.
Nice to have
• Tagline

```html
<!DOCTYPE html>
<html lang="en">
<head>
<meta charset="utf-8">
<title>Harwick Stone Meadows Golf Club – Billboard</title>
<link rel="stylesheet" href="https://fonts.googleapis.com/css2?family=Passion+One:wght@400&family=Roboto+Condensed:wght@700&display=swap">
<style>
  :root {
    --page-bg: #e9ecef;
    --board-white: #ffffff;
    --grass-dark: #3f6e2a;
    --grass-mid: #6b9a45;
    --panel-green: #6aab3a;
    --panel-lime: #a5cc5b;
    --panel-yellow: #f5c219;
    --brand-green: #1b9a3e;
    --tagline-white: #ffffff;
  }
  * { box-sizing: border-box; margin: 0; padding: 0; }
  html, body {
    width: 1200px;
    height: 901px;
    overflow: hidden;
    background: var(--page-bg);
  }
  .billboard {
    position: absolute;
    left: 50px;
    top: 246px;
    width: 1100px;
    height: 408px;
    background: var(--board-white);
    box-shadow: 0 6px 24px rgba(0,0,0,0.18);
  }
  .billboard__band {
    position: absolute;
    left: 0;
    top: 62px;
    width: 100%;
    height: 274px;
    display: flex;
  }
  .band__photo {
    width: 433px;
    height: 100%;
    background: radial-gradient(ellipse at 45% 55%, var(--grass-mid), var(--grass-dark));
  }
  .band__green {
    position: relative;
    width: 267px;
    height: 100%;
    background: var(--panel-green);
  }
  .band__lime {
    width: 265px;
    height: 100%;
    background: var(--panel-lime);
  }
  .band__yellow {
    flex: 1;
    height: 100%;
    background: var(--panel-yellow);
  }
  .tagline {
    position: absolute;
    left: 21px;
    top: 128px;
    font-family: "Passion One", "Arial Black", sans-serif;
    font-weight: 400;
    font-size: 45px;
    line-height: 38px;
    color: var(--tagline-white);
    text-shadow: 2px 2px 3px rgba(0,0,0,0.45);
  }
  .billboard__footer {
    position: absolute;
    left: 0;
    top: 336px;
    width: 100%;
    height: 72px;
    display: flex;
    align-items: center;
    justify-content: space-between;
    padding: 0 34px 0 30px;
    font-family: "Roboto Condensed", "Arial Narrow", sans-serif;
    font-weight: 700;
    color: var(--brand-green);
  }
  .directions {
    display: flex;
    align-items: center;
    gap: 14px;
    font-size: 27px;
    line-height: 1;
  }
  .directions__icon { width: 42px; height: 42px; flex: none; }
  .brand {
    display: flex;
    align-items: center;
    gap: 10px;
    font-size: 24px;
    line-height: 1;
  }
  .brand__dot {
    width: 30px;
    height: 30px;
    border-radius: 50%;
    background: var(--brand-green);
    flex: none;
  }
</style>
</head>
<body>
  <section class="billboard" aria-label="Harwick Stone Meadows Golf Club billboard">
    <div class="billboard__band">
      <div class="band__photo" role="img" aria-label="Close-up photo of a hand placing a golf ball on a tee in green grass"></div>
      <div class="band__green">
        <p class="tagline">Your<br>Daily Dose<br>of Iron</p>
      </div>
      <div class="band__lime"></div>
      <div class="band__yellow"></div>
    </div>

    <div class="billboard__footer">
      <div class="directions">
        <svg class="directions__icon" viewBox="0 0 42 42" aria-hidden="true">
          <circle cx="21" cy="21" r="20" fill="#1b9a3e"/>
          <path d="M25 11 L14 21 L25 31" fill="none" stroke="#ffffff" stroke-width="5" stroke-linecap="round" stroke-linejoin="round"/>
        </svg>
        <span>Turn Left onto 212S - 6 Miles</span>
      </div>

      <div class="brand">
        <span class="brand__dot" aria-hidden="true"></span>
        <span class="brand__name">Harwick Stone Meadows Golf Club</span>
      </div>
    </div>
  </section>
</body>
</html>
```